Aged Care Consultancy Business needs a business card design

I need a two sided business card - I want it clean and professional. Surprise me

Target Market(s)

middle aged and ageing victorians

Industry/Entity Type

Health Care

Contact Information for Business Card

Text to be included

Logo
Aged Care Consulting Services
Professional, Reliable, Affordable

Orin Tessaldo
Director
0472 31 64 09 (larger)
1300 31 64 09
orin@valtrino.com.au
www.valtrinocare.com.au
Facebook (details TBA)

include little icons beside the contact info:

- Envelope = email
- Phone = phone
- Globe = website

Font styles to use
Serif
Sans Serif

Requirements
Must have
• look proffesional and clean

```html
<!DOCTYPE html>
<html lang="en">
<head>
<meta charset="utf-8">
<title>Valtrino Care – Business Card</title>
<link rel="stylesheet" href="https://fonts.googleapis.com/css2?family=Arimo:wght@400;700&display=swap">
<style>
  :root {
    --page-bg: #d9d6d2;
    --card-black: #141415;
    --card-edge: #1d1d1f;
    --emboss-grey: #3a3a3c;
    --tagline-grey: #8c8c8e;
    --brand-blue: #1f5fae;
    --brand-orange: #e8952a;
    --text-white: #f2f2f2;
    --divider: #5a5a5c;
  }
  * { margin: 0; padding: 0; box-sizing: border-box; }
  html, body {
    width: 1200px; height: 864px; overflow: hidden;
    background: var(--page-bg);
    font-family: "Arimo", Arial, sans-serif;
  }
  .sheet {
    width: 1200px; height: 864px;
    display: flex; flex-direction: column;
    align-items: center; justify-content: center; gap: 36px;
  }
  .card {
    width: 620px; height: 379px;
    background: var(--card-black);
    border: 1px solid var(--card-edge);
    border-radius: 4px;
    position: relative;
    box-shadow: 0 6px 18px rgba(0,0,0,.25);
  }

  /* Front */
  .card-front .brand-name {
    position: absolute; left: 0; right: 0; top: 130px;
    text-align: center;
    font-size: 52px; font-weight: 700; letter-spacing: -1px;
    color: var(--emboss-grey);
  }
  .card-front .tagline {
    position: absolute; left: 30px; bottom: 34px;
    font-size: 13px; color: var(--tagline-grey);
  }

  /* Back */
  .card-back .brand-name {
    position: absolute; left: 44px; top: 168px; width: 240px;
    text-align: center;
    font-size: 40px; font-weight: 700; letter-spacing: -1px;
    color: var(--brand-blue);
  }
  .card-back .divider {
    position: absolute; left: 318px; top: 70px;
    width: 1px; height: 240px;
    background: linear-gradient(to bottom, transparent, var(--divider) 20%, var(--divider) 80%, transparent);
  }
  .contact {
    position: absolute; left: 346px; top: 92px;
    color: var(--text-white);
  }
  .contact .person-name { font-size: 18px; color: var(--brand-blue); }
  .contact .person-role { font-size: 14px; color: var(--brand-orange); margin-bottom: 18px; }
  .contact-list { list-style: none; }
  .contact-list li {
    display: flex; align-items: center; gap: 10px;
    font-size: 14px; line-height: 22px;
  }
  .contact-list li.primary-phone { font-size: 24px; line-height: 34px; }
  .contact-list svg { width: 14px; height: 14px; flex: none; fill: var(--brand-blue); }
</style>
</head>
<body>
<main class="sheet">
  <section class="card card-front">
    <div class="brand-name">valtrino care</div>
    <p class="tagline">Aged Care Consulting Services, Professional, Reliable, Affordable</p>
  </section>

  <section class="card card-back">
    <div class="brand-name">valtrino care</div>
    <div class="divider"></div>
    <div class="contact">
      <p class="person-name">Orin Tessaldo</p>
      <p class="person-role">Director</p>
      <ul class="contact-list">
        <li class="primary-phone">
          <svg viewBox="0 0 16 16"><path d="M3 1h3l1 4-2 1c1 2 3 4 5 5l1-2 4 1v3c0 1-1 2-2 2C7 15 1 9 1 3c0-1 1-2 2-2z"/></svg>
          0472 31 64 09
        </li>
        <li>
          <svg viewBox="0 0 16 16"><path d="M3 1h3l1 4-2 1c1 2 3 4 5 5l1-2 4 1v3c0 1-1 2-2 2C7 15 1 9 1 3c0-1 1-2 2-2z"/></svg>
          1300 31 64 09
        </li>
        <li>
          <svg viewBox="0 0 16 16"><path d="M1 3h14v10H1z M1 3l7 6 7-6" fill="none" stroke="#1f5fae" stroke-width="1.6"/></svg>
          orin@valtrino.com.au
        </li>
        <li>
          <svg viewBox="0 0 16 16"><g fill="none" stroke="#1f5fae" stroke-width="1.4"><circle cx="8" cy="8" r="6.5"/><ellipse cx="8" cy="8" rx="3" ry="6.5"/><path d="M1.5 8h13"/></g></svg>
          www.valtrinocare.com.au
        </li>
        <li>
          <svg viewBox="0 0 16 16"><rect x="1" y="1" width="14" height="14" rx="2"/></svg>
          valtrinocare
        </li>
      </ul>
    </div>
  </section>
</main>
</body>
</html>
```